We host an educational conference for physicians each year, but this year is our *90th year* so we're going big. We have decided to add break-out sessions (tracks) to our conference, which is usually only one track and held in only one room.

Each year we mail out a brochure, and I have attached last year's as a reference (see "2017 Brochure" attachment). Also attached is a copy of the Save The Date we did earlier this year, so it would be nice if this brochure was similar to that design, but it's not necessary.

I have attached a sample of the type of agenda (table) I am looking for, but we obviously want it to look much nicer than this. The lectures in the GREEN are plenary sessions (all attendees together in the same room), and the lectures in BLUE are break-out sessions (attendees go to separate rooms).

This brochure will be three events rolled into one, with the Scientific Session being the most prominent.

* EVENT NAMES:
"The 90th Annual Scientific Session"
"The 28th Annual Meeting"
"The 2nd Annual New York FIT Trivium Competition"

* SIZE: In the past, we have done a double-gate fold, which is 22.5" wide x 8.5" tall (double-sided art) that the printer folds down to 5.5" x 8.5" (with space for the stamp and address. Your art can be smaller but not larger. It should be able to fold and have space for an address to be printed.

* CONTENT: In addition to the agenda/table, there will need to be a "cover," room for the faculty names and their organizations, room for the Program Description, room for the Target Audience, room for the Program Objectives, room for the boards of directors (3), room for registration rates, room for the Physician Continuing Medical Education section, room for the Disclosure of Conflicts of Interest section, room for the RJT section and QLV section (with logos), room for how-to-register information and room for the Trivium event details (and address and cost).

* LOGOS: We will need to have our CHAPTER logo, SOCIETY logo, "90th" logo, Brightwater Heart Institute logo, and the QLV logo somewhere on the document.

* IMAGERY: I have high-resolution photos of past Annual Meetings and Trivium events if needed. It's not crucial that this brochure have pictures though.

* MORE INFO:
Scientific Session event page: http://tk-hvs.example/annualmtg18/
FIT Trivium event page: http://tk-hvs.example/cocktail-reception-and-fit-quizbowl/

Target Market(s)

Brochure will be mailed to our members

Industry/Entity Type

Medicine

Requirements
Must have
• Must have a "table," design or infographic that clearly shows the schedule of events (plenary sessions and break-out sessions). Must have event names, room for faculty names and their organizations, the Program Description, the Target Audience, the Program Objectives, the 3 boards of directors, registration rates, the CME info section, the Disclosure of COI info, the RJT section and QLV section (both with logos), how-to-register information and the Trivium event details (with room for the address and cost details).
• * SIZE: In the past, we have done a double-gate fold, which is 22.5" wide x 8.5" tall (double-sided art) that the printer folds down to 5.5" x 8.5" (with space for the stamp and address. Your art can be smaller but not larger. It should be able to fold and have space for an address to be printed.
• * LOGOS: We will need to have our CHAPTER logo, SOCIETY logo, "90th" logo, Brightwater Heart Institute logo, and the QLV logo somewhere on the document.
Nice to have
• Nice to have a design that looks somewhat similar to the Save The Date that was sent out (attached, "SaveTheDate_sourcefile")
Should not have
• Should not have stock imagery of people or be too cartoonish. These are physicians, many at the very top of their field, and this is their annual, professional educational event. Even though it's our 90th "birthday," this is not a party and should not look too celebratory.

```html
<!DOCTYPE html>
<html lang="en">
<head>
<meta charset="utf-8">
<title>Program Table – Scientific Session Brochure</title>
<link href="https://fonts.googleapis.com/css2?family=Open+Sans:ital,wght@0,400;0,600;0,700;0,800;1,400;1,600;1,700;1,800&display=swap" rel="stylesheet">
<style>
:root{
  --navy:#1b3561;
  --navy-deep:#162c52;
  --ink:#1a1a1a;
  --cell-blue:#dbe8f6;
  --rule:#3d4f72;
  --gold:#c6b27a;
  --sand:#ccc6ad;
  --paper:#ffffff;
  --stage:#e9e9e9;
  --text-soft:#20345a;
}
*{box-sizing:border-box;margin:0;padding:0}
html,body{width:1200px;height:562px;overflow:hidden;background:var(--stage)}
body{font-family:"Open Sans",Arial,sans-serif;color:var(--ink)}
.spread{position:relative;width:1200px;height:562px;background:linear-gradient(90deg,#2a4270 0,var(--navy) 6%,var(--navy) 100%)}
.rates-column{position:absolute;left:1069px;top:0;width:131px;height:562px;background:var(--sand);padding:22px 8px 0 10px;color:var(--navy)}
.inner-panel{position:absolute;left:32px;top:34px;width:1007px;height:491px;background:var(--paper);outline:1px solid var(--gold);outline-offset:2px}

/* left info column */
.info-column{position:absolute;left:0;top:14px;width:145px;padding-left:12px;padding-right:4px;font-size:6.3px;line-height:7.9px;color:var(--navy)}
.info-column h3{font-size:7.2px;line-height:8px;font-weight:700;color:var(--navy);margin-bottom:1px}
.info-column p{margin-bottom:6px}
.info-column .block{margin-bottom:4px}
.partner-mark{display:flex;align-items:center;gap:5px;margin:4px 0 8px}
.partner-mark .dot{width:16px;height:16px;border-radius:50%;background:var(--navy);flex:none}
.partner-mark span{font-size:6.5px;line-height:7.5px;color:var(--navy);border-left:1px solid var(--navy);padding-left:5px}
.access-row{display:flex;gap:6px}
.access-row .icon{flex:none;margin-top:1px}
.committee{line-height:7.3px}
.divider{position:absolute;top:14px;bottom:14px;border-left:1px dotted var(--gold)}
.divider.left{left:145px}
.divider.right{left:792px}

/* program table */
.program-title{position:absolute;left:162px;top:19px;font-size:24px;font-weight:800;font-style:italic;color:var(--navy);letter-spacing:-.2px}
.program-table{position:absolute;left:160px;top:82px;width:625px;border:1px solid var(--rule);font-size:7.1px;line-height:8.8px}
.row{display:flex;border-bottom:1px solid var(--rule)}
.row:last-child{border-bottom:none}
.time{width:59px;flex:none;display:flex;align-items:center;justify-content:center;background:var(--paper);border-right:1px solid var(--rule);font-size:6.8px}
.slot{flex:1;display:flex;align-items:center;padding:0 8px;background:var(--paper)}
.slot.plenary{background:var(--cell-blue)}
.slot + .slot{border-left:1px solid var(--rule)}
.slot b{font-weight:700}
.slot i{font-style:italic}
.slot .title{font-weight:700;font-style:italic}
.stack{display:block}
.r25{height:25px}.r26{height:26px}.r27{height:27px}.r42{height:42px}.r49{height:49px}.r29{height:29px}.r74{height:74px}.r47{height:47px}

/* faculty */
.faculty{position:absolute;left:812px;top:92px;width:192px;color:var(--navy)}
.faculty h2{font-size:9px;font-weight:700;letter-spacing:.3px;margin-bottom:6px}
.faculty-member{font-size:6.3px;line-height:7.4px;margin-bottom:7.4px}
.faculty-member .name{font-weight:700;text-transform:uppercase;font-size:6.6px}
.faculty-member .role{font-style:italic}
.heart-art{position:absolute;right:0;top:0;width:100px;height:148px;background:radial-gradient(ellipse at 55% 45%,#e4e8f1 0,#eef1f6 45%,rgba(255,255,255,0) 75%)}

/* rates column */
.rates-column h3{font-size:7.8px;line-height:8.6px;font-weight:700;margin-bottom:6px}
.rates-column .note{font-style:italic;font-size:6px;line-height:7.2px;margin-bottom:3px}
.rates-column .fee{font-size:6px;line-height:7.2px;margin-bottom:3px}
.rates-column .group{margin-bottom:8px}
.rates-column .walkin{font-style:italic;font-weight:600;font-size:6px;margin:4px 0 14px}
.rates-column .fine{font-style:italic;font-size:5.6px;line-height:6.8px;margin-bottom:12px}
</style>
</head>
<body>
<main class="spread">

  <section class="inner-panel">

    <aside class="info-column">
      <div class="block">
        <h3>Physician Continuing Medical Education</h3>
        <p>This activity has been planned and implemented in accordance with the accreditation requirements and policies of the Board for Continuing Clinical Education (BCCE) through the joint providership of Quillfield Learning Ventures and The Tidewater Cardiovascular Society. Quillfield Learning Ventures is accredited by the BCCE to provide continuing medical education for physicians. Quillfield Learning Ventures designates this live activity for a maximum of <i>7.0 BCCE Category 1 Credit(s)™</i>. Physicians should claim only the credit commensurate with the extent of their participation in the activity.</p>
      </div>
      <div class="block">
        <h3>Disclosure of Conflicts of Interest</h3>
        <p>Quillfield Learning Ventures (QLV) requires instructors, planners, managers and other individuals who are in a position to control the content of this activity to disclose any real or apparent conflict of interest (COI) they may have as related to the content of this activity. All identified COI are thoroughly vetted and resolved according to QLV policy. The existence or absence of COI for everyone in a position to control content will be disclosed to participants prior to the start of each activity.</p>
        <p>This activity is jointly provided by Quillfield Learning Ventures and The Tidewater Cardiovascular Society.</p>
      </div>
      <div class="partner-mark">
        <div class="dot"></div>
        <span>Quillfield Learning<br>Ventures</span>
      </div>
      <div class="block">
        <h3>RJT Accessibility Services</h3>
        <div class="access-row">
          <svg class="icon" width="14" height="14" viewBox="0 0 14 14" aria-hidden="true"><rect width="14" height="14" fill="var(--navy)"/></svg>
          <p>Event staff will be glad to assist you with any special needs (i.e., physical, dietary, etc). Contact us prior to the live event at (555) 014-0228.</p>
        </div>
      </div>
      <div class="block committee">
        <h3>Planning Committee</h3>
        Lorna P. Haverick, MD, FACC<br>
        Martin C. Dowell, MD, FACC<br>
        Gregory L. Tamsen, MD, FACC<br>
        Tomás E. Varela, MD, FACC, FAHA<br>
        J. Dale Ferrand, MD, FACC
      </div>
    </aside>

    <div class="divider left"></div>

    <h1 class="program-title">Program Table</h1>

    <div class="program-table">
      <div class="row r25"><div class="time">9:00 a.m.</div><div class="slot plenary">Registration&nbsp;<b>Auditorium</b></div></div>
      <div class="row r26"><div class="time">9:30 a.m.</div><div class="slot"><span><b>Welcome</b> <i>(Auditorium, holds 160 people)</i> Lorna P. Haverick, MD, FACC | J. Dale Ferrand, MD, FACC</span></div></div>
      <div class="row r26"><div class="time">9:45 a.m.</div><div class="slot plenary"><span><b>Morning Plenary &nbsp;"A" Lecture</b> <i>(Auditorium, holds 160 people)</i> <span class="title">"PSCK9 Inhibitors in Dyslipidemia"</span> &nbsp;Marisa Coldwell, MD, MPH</span></div></div>
      <div class="row r27"><div class="time">10:45 a.m.</div><div class="slot"><span><b>Morning Plenary "B" Lecture</b> <i>(Auditorium, holds 160 people)</i> Edwin R. Sallow, MD, MBA, FACC</span></div></div>
      <div class="row r42"><div class="time">11:00 a.m.</div><div class="slot plenary"><span><b>Morning Breakout "A" Lecture</b> <i>(Room C198, holds 64 people)</i> <b>"MACRA/QPP Update – is "MIPS or MOOPS? Lessons Learned from Year 1 of the Quality Payment Program and What'sin Store for the Future"</b> <i>Delia Okafor</i></span></div></div>
      <div class="row r49"><div class="time">11:30 a.m.</div>
        <div class="slot" style="flex:0 0 262px"><span><b>Morning Breakout "B" Lecture</b> <i>(Room 9204, holds 32 people)</i><br><b>[Tentative] "Negotiating Contracts"</b></span></div>
        <div class="slot" style="padding-left:34px"><span><b>Morning Breakout "C" Lecture</b> <i>(Room 9205, holds 32 people)</i><br><b>"Journal Club: Summary of the Top Trials of 2018"</b></span></div>
      </div>
      <div class="row r26"><div class="time">12:30 p.m.</div><div class="slot plenary"><span><b>Lunch 'n' Learn</b> &nbsp;<i>(RoomsC201, C202, C203, C204&amp;C205)</i></span></div></div>
      <div class="row r26"><div class="time">1:45 p.m.</div><div class="slot"><span><b>Keynote Plenary Lecture</b> <i>(Auditorium, holds 160 people)</i> Anselm Varga, MD, PhD, MACC</span></div></div>
      <div class="row r29"><div class="time">2:30 p.m.</div><div class="slot plenary"><span><b>Case Presentations</b> <i>(Auditorium, holds 160 people)</i></span></div></div>
      <div class="row r74"><div class="time">3:30 p.m.</div>
        <div class="slot" style="flex:0 0 168px"><span><b>Afternoon Breakout "A" Lecture</b><br><i>(Room C198, holds 64 people)</i><br><b>"Career Pathways &nbsp;(Title Needed)"</b><br><i>Dale Ferrand</i></span></div>
        <div class="slot" style="flex:0 0 202px"><span><b>Afternoon Breakout "B" Lecture</b><br><i>(Room 9204, holds 32 people)</i> <b>Management of Bleeding w/ Direct-Acting Oral Anticoagulants"</b> <i>Ruth Pellam</i> (CONFIRMED)</span></div>
        <div class="slot" style="padding-left:18px"><span><b>Afternoon Breakout "C" Lecture</b><br><i>(Room 9205, holds 32 people)</i> &nbsp;<b>"Effective Leadership Styles"</b><br><i>w/ Lorna P. Haverick</i></span></div>
      </div>
      <div class="row r47"><div class="time">4:30 p.m.</div>
        <div class="slot plenary" style="flex:0 0 283px"><span><b>Afternoon Plenary Lecture</b> <i>(Auditorium, holds 160 ppl)</i><br><i>Gwen Alder</i></span></div>
        <div class="slot plenary"><span><b>Awards, Announcements &amp; Closing</b> <i>(Auditorium, holds 160 ppl)</i><br><i>Drs. Haverick &amp; Ferrand</i></span></div>
      </div>
    </div>

    <div class="divider right"></div>

    <div class="heart-art" role="img" aria-label="Faint engraved heart illustration as background decoration"></div>

    <section class="faculty">
      <h2>FACULTY</h2>
      <div class="faculty-member"><div class="name">Harold T. Brennick III, MD, FACC</div><div class="role">Emeritus Professor of Medicine</div><div>Westmere School of Medicine</div><div class="role">Former Chief of the Division of Cardiology</div><div>Larchmont Valley Medical Center</div></div>
      <div class="faculty-member"><div class="name">R. Ansel Pike, MD, MBA, FACC</div><div class="role">Director, The Robotic Cardiac Surgery Program</div><div>Harborview Union Medical Center</div></div>
      <div class="faculty-member"><div class="name">Martin C. Dowell, MD, FACC</div><div class="role">Director of Cardiac Catheterization Laboratories and Professor of Medicine</div><div>Pinecrest University Hospital</div></div>
      <div class="faculty-member"><div class="name">Gregory L. Tamsen, MD, FACC</div><div class="role">Director, Lakeshore Branch</div><div>Ridgeline Heart Institute</div></div>
      <div class="faculty-member"><div class="name">Rodrigo A. Salas, MD, PhD, FACC, FSIAC, FESC</div><div class="role">Governor of the Marisol Chapter of the HVS<br>Professor of Medicine</div><div>University of San Alba</div></div>
      <div class="faculty-member"><div class="name">Tomás E. Varela, MD, FACC, FAHA</div><div class="role">Chief of Cardiology</div><div>Northfield Medical Center</div></div>
      <div class="faculty-member"><div class="name">Kevin H. Ro, MD, PhD</div><div class="role">Assistant Professor of Medicine, Cardiac Electrophysiology</div><div>Easton Cardiac Electrophysiology Associates</div></div>
      <div class="faculty-member"><div class="name">Mateo J. Ortiz, MD, FACC</div><div class="role">Past President of the Southern Federation of Cardiology<br>Chief of Clinical Cardiology</div><div>Hospital San Marco (Alameda)</div></div>
      <div class="faculty-member"><div class="name">Anne B. Lindqvist, MD</div><div class="role">Assistant Professor of Medicine-Cardiology</div><div>Lakeview University School of Medicine</div></div>
    </section>
  </section>

  <aside class="rates-column">
    <h3>Scientific Session / Annual Meeting Registration Fees</h3>
    <div class="group">
      <div class="note">"Early-Bird" Rates (Before 10/2/17):</div>
      <div class="fee">TKACC / HVS / Marisol Member (Physician) – $75</div>
      <div class="fee">TKACC / HVS / Marisol Member (CVT / Other) – $35</div>
      <div class="fee">Non-Member (Physician) – $150</div>
      <div class="fee">Non-Member (CVT / Other) – $70</div>
      <div class="fee">FITs &amp; Residents – Free (pre-registration required)</div>
    </div>
    <div class="group">
      <div class="note">Regular Rates (On or after 10/2/17):</div>
      <div class="fee">TKACC / HVS / Marisol Member (Physician) – $100</div>
      <div class="fee">TKACC / HVS / Marisol Member (CVT / Other) – $55</div>
      <div class="fee">Non-Member (Physician) – $175</div>
      <div class="fee">Non-Member (CVT / Other) – $90</div>
      <div class="fee">FITs and Residents – Free (pre-registration required)</div>
    </div>
    <div class="walkin">Scientific Session Walk-in Rate - $199</div>

    <h3>Inaugural NY FIT Trivium Competition, Cocktail Reception &amp; Whiskey Tasting</h3>
    <div class="group">
      <div class="note">Dec. 6, 2017, 6:30 - 10:30 p.m.</div>
      <div class="fee">TKACC / HVS / Marisol Member – Free (pre-registration required)</div>
      <div class="fee">Non-Members / Guests – $30</div>
    </div>

    <h3>Women in Cardiology (WIC) Networking Event**</h3>
    <div class="group">
      <div class="note">Dec. 7, 2017, 4:30 - 6:30 p.m.</div>
      <div class="fee">Physicians – $20</div>
      <div class="fee">FITs &amp; Residents – $10</div>
    </div>
    <div class="fine">** Note: The WIC Networking Event is intended for women physicians. Admission is <b>free</b> to those who attend the all-day Scientific Session (pre-registration required)</div>

    <h3 style="margin-bottom:2px">Additional Information</h3>
    <div class="fee">For more information or to inquire about becoming a sponsor or exhibitor, send an email to ask@tk-hvs.example or call (555) 014-0228.</div>
  </aside>

</main>
</body>
</html>
```